Everything fresh, everything new

When I take over the practice, I would like to breathe new life into the practice. I want a business card design that catches the eye and brings a breath of fresh air

```html
<!DOCTYPE html>
<html lang="en">
<head>
<meta charset="utf-8">
<title>Vitalpunkt – Business Card</title>
<link rel="stylesheet" href="https://fonts.googleapis.com/css2?family=Montserrat:wght@300;400;500;600&display=swap">
<style>
  :root {
    --charcoal: #4a4b4d;
    --lime: #7cc242;
    --white: #ffffff;
    --paper: #ffffff;
    --backdrop: #b8b8b8;
    --ink: #4a4b4d;
    --ink-soft: #5a5b5d;
  }
  * { margin: 0; padding: 0; box-sizing: border-box; }
  html, body {
    width: 1200px; height: 1200px; overflow: hidden;
    background: var(--backdrop);
    font-family: "Montserrat", sans-serif;
  }
  .canvas { position: relative; width: 1200px; height: 1200px; }

  .card {
    position: absolute; left: 194px; width: 811px; height: 464px; overflow: hidden;
  }
  .card--front { top: 83px; background: var(--charcoal); }
  .card--back { top: 654px; background: var(--paper); }

  .bar { position: absolute; }
  .bar--side { top: 49px; width: 14px; height: 365px; }
  .bar--left { left: 0; }
  .bar--right { right: 0; }
  .bar--lime { background: var(--lime); }
  .bar--white { background: var(--white); }
  .bar--charcoal { background: var(--charcoal); }

  .rule { position: absolute; height: 2px; width: 142px; }
  .rule--top { left: 51px; top: 26px; background: var(--white); }
  .rule--bottom { left: 618px; top: 435px; height: 3px; background: var(--lime); }

  .brand {
    position: absolute; display: flex; align-items: center; gap: 14px;
    transform: translate(-50%, -50%); white-space: nowrap;
  }
  .brand__dot { border-radius: 50%; background: var(--lime); flex: none; }
  .brand__name { font-weight: 500; letter-spacing: 0.5px; }

  .card--front .brand { left: 405px; top: 232px; }
  .card--front .brand__dot { width: 26px; height: 26px; }
  .card--front .brand__name { font-size: 58px; color: var(--white); }

  .front-email {
    position: absolute; left: 0; right: 0; top: 420px; text-align: center;
    color: var(--white); font-size: 14px; font-weight: 500; letter-spacing: 3.2px;
  }

  .divider { position: absolute; left: 405px; top: 53px; width: 2px; height: 355px; background: var(--lime); }

  .identity { position: absolute; right: 471px; top: 96px; text-align: right; }
  .identity__name { font-size: 23px; font-weight: 600; color: var(--ink); letter-spacing: 0.3px; line-height: 1.2; }
  .identity__role {
    display: inline-block; font-size: 18px; font-weight: 300; color: var(--ink-soft);
    line-height: 1.3; margin-top: 1px;
  }
  .identity__role span { border-bottom: 2px solid var(--lime); padding-bottom: 1px; }

  .contacts { position: absolute; right: 471px; top: 200px; list-style: none; }
  .contact {
    display: flex; align-items: center; justify-content: flex-end; gap: 17px;
    font-size: 15px; font-weight: 400; color: var(--ink); line-height: 1.45;
    text-align: right; margin-bottom: 13px;
  }
  .contact--address { margin-bottom: 16px; }
  .contact__icon {
    width: 23px; height: 23px; border-radius: 4px; flex: none;
    display: flex; align-items: center; justify-content: center; background: var(--lime);
  }
  .contact__icon--dark { background: var(--charcoal); }
  .contact__icon svg { width: 14px; height: 14px; fill: var(--white); }

  .card--back .brand { left: 598px; top: 233px; gap: 10px; }
  .card--back .brand__dot { width: 14px; height: 14px; }
  .card--back .brand__name { font-size: 32px; color: var(--ink); }
</style>
</head>
<body>
<main class="canvas">

  <section class="card card--front" aria-label="Business card front">
    <div class="rule rule--top"></div>
    <div class="bar bar--side bar--left bar--lime"></div>
    <div class="bar bar--side bar--right bar--white"></div>
    <div class="brand">
      <span class="brand__dot"></span>
      <span class="brand__name">Vitalpunkt</span>
    </div>
    <p class="front-email">hello@vitalpunkt.com</p>
    <div class="rule rule--bottom"></div>
  </section>

  <section class="card card--back" aria-label="Business card back">
    <div class="bar bar--side bar--left bar--charcoal"></div>
    <div class="bar bar--side bar--right bar--lime"></div>

    <div class="identity">
      <h1 class="identity__name">MARTIN K. SANDER</h1>
      <p class="identity__role">Managing <span>Director</span></p>
    </div>

    <ul class="contacts">
      <li class="contact contact--address">
        <span>2317 Lindenhof Avenue<br>Fairview, OR 97024</span>
        <span class="contact__icon contact__icon--dark">
          <svg viewBox="0 0 24 24"><path d="M12 2a7 7 0 0 0-7 7c0 5 7 13 7 13s7-8 7-13a7 7 0 0 0-7-7zm0 9.5A2.5 2.5 0 1 1 12 6.5a2.5 2.5 0 0 1 0 5z"/></svg>
        </span>
      </li>
      <li class="contact">
        <span>+00 987 654 32</span>
        <span class="contact__icon">
          <svg viewBox="0 0 24 24"><path d="M6.6 10.8a15 15 0 0 0 6.6 6.6l2.2-2.2a1 1 0 0 1 1-.25 11.4 11.4 0 0 0 3.6.57 1 1 0 0 1 1 1V20a1 1 0 0 1-1 1A17 17 0 0 1 3 4a1 1 0 0 1 1-1h3.5a1 1 0 0 1 1 1c0 1.25.2 2.45.57 3.6a1 1 0 0 1-.25 1z"/></svg>
        </span>
      </li>
      <li class="contact">
        <span>hello@vitalpunkt.com</span>
        <span class="contact__icon">
          <svg viewBox="0 0 24 24"><path d="M2 5h20v14H2zm2 2v.4l8 5 8-5V7zm0 2.8V17h16V9.8l-8 5z"/></svg>
        </span>
      </li>
      <li class="contact">
        <span>www.vitalpunkt-praxis.com</span>
        <span class="contact__icon">
          <svg viewBox="0 0 24 24"><path d="M6 2l13 11.5-5.6.6 3.3 6.8-2.6 1.2-3.2-6.9L6 19z"/></svg>
        </span>
      </li>
    </ul>

    <div class="divider"></div>

    <div class="brand">
      <span class="brand__dot"></span>
      <span class="brand__name">Vitalpunkt</span>
    </div>
  </section>

</main>
</body>
</html>
```